VeloRoot Sample Packaging Design

We need a design - with assistance on logo and colours - of a box containing sample sachets of a new natural sports supplement for endurance athletes.
We have an idea of logo and colours but would like input, ideas and assistance to create a cool new brand.

The product is based on natural beetroot powder which is scientifically backed to improve sports performance.
We like clean minimal branding that looks scientific - such as Qvx Dietics, Heap Grains, Brain Den Max and TuK Gamma Burn sachets.

Attached is the type of package we will be using with matt black sachets, so clean white with potentially a beetroot colour (hex 691a40??) and grey (a3b2c2??) but we would like your professional and creative input.

I have attached a rough logo mock up of the logo I designed, happy for you to develop this by making it a bit cleaner (left edges angled or curved maybe- change font also maybe??) or your own ideas if clean, simple and effective. I based mine off the Swift Arrow logo and PB works well with VeloRoot and Personal Best.

The final design should be clean, minimalist, high end sports supplement with a science and natural beetroot feel.
Box size: 300mm x 130mm x 14mm

Target Market(s)

Elite athletes and professionals wanting natural and science-backed supplements that work. Probably mainly men.
The customers are long distance sportspeople and NOT bodybuilders! Including triathletes, cyclists, long distance runners and swimmers.
The brand must also appeal to club level athletes and weekend warriors (but this should be easy if it's targeted at elite level first)

Industry/Entity Type

Supplement

Font styles to use
Sans Serif

Colors

Designer to choose colors to be used in the design.

Requirements
Must have
• - New logo (I like the Swift Arrow logo but open to new ideas!)
• - Clean, scientific look with a twist of "I'm natural and not full of sports supplement junk!!"
• - A shade of beetroot red/purple as the signature colour, without looking too feminine.
• - Our slogan is "Beat your best"
Should not have
• A bodybuilder look.

```html
<!DOCTYPE html>
<html lang="en">
<head>
<meta charset="utf-8">
<title>VeloRoot Beetroot Nitrate Supplement – Box and Sachet</title>
<link rel="stylesheet" href="https://fonts.googleapis.com/css2?family=Bebas+Neue&family=Montserrat:wght@300;400&display=swap">
<style>
  :root {
    --stage: #ececec;
    --box-black: #211f20;
    --box-edge: #4a4a4a;
    --lime: #c9d22a;
    --beet: #b42a5c;
    --white: #ffffff;
    --sachet-white: #f4f4f4;
    --sachet-ink: #3a3a3a;
  }
  * { margin: 0; padding: 0; box-sizing: border-box; }
  html, body {
    width: 1200px; height: 507px; overflow: hidden;
    background: var(--stage);
  }
  .canvas { position: relative; width: 1200px; height: 507px; }

  /* ---------- Box front ---------- */
  .box {
    position: absolute; left: 91px; top: 71px;
    width: 773px; height: 358px;
    background: var(--box-black);
    border-left: 6px solid var(--box-edge);
    border-right: 6px solid var(--box-edge);
  }
  .brand {
    position: absolute; display: flex; align-items: center;
    font-family: "Montserrat", sans-serif; font-weight: 300;
    color: var(--white);
  }
  .brand-dot { border-radius: 50%; border: 4px solid var(--white); }
  .box .brand { left: 52px; top: 50px; gap: 24px; font-size: 23px; letter-spacing: 6px; }
  .box .brand-dot { width: 48px; height: 48px; }

  .headline {
    position: absolute; font-family: "Bebas Neue", sans-serif;
    font-weight: 400; text-transform: uppercase;
  }
  .box .headline {
    left: 58px; top: 150px; font-size: 51px; line-height: 41px;
    color: var(--lime); letter-spacing: 0.5px;
  }
  .tagline {
    position: absolute; display: flex; align-items: center;
    font-family: "Montserrat", sans-serif; font-weight: 400;
  }
  .tagline .sep { display: inline-block; width: 1px; background: currentColor; }
  .box .tagline { left: 64px; top: 250px; font-size: 18px; color: var(--white); gap: 9px; }
  .box .tagline .sep { height: 24px; }
  .count {
    position: absolute; left: 64px; top: 290px;
    font-family: "Bebas Neue", sans-serif; font-size: 24px;
    color: var(--lime); letter-spacing: 0.5px;
  }
  .sport-icons { position: absolute; left: 531px; top: 312px; display: flex; gap: 1px; }
  .sport-icons span {
    width: 27px; height: 27px; border-radius: 50%;
    border: 1.5px solid var(--white);
  }
  .beet-illustration {
    position: absolute; left: 640px; top: 193px; width: 102px; height: 157px;
    background: radial-gradient(ellipse at 45% 70%, var(--beet) 0 45%, #9e2350 70%, transparent 72%);
  }

  /* ---------- Sachet ---------- */
  .sachet {
    position: absolute; left: 974px; top: 107px; width: 189px; height: 312px;
  }
  .sachet-face { position: absolute; inset: 0; }
  .sachet .brand { left: 0; right: 0; top: 42px; flex-direction: column; gap: 6px; font-size: 12px; letter-spacing: 3px; }
  .sachet .brand-dot { width: 24px; height: 24px; border-width: 3px; }
  .sachet .headline {
    right: 26px; top: 198px; font-size: 18px; line-height: 16px;
    color: var(--beet); text-align: right;
  }
  .sachet .tagline { right: 8px; top: 236px; font-size: 9px; color: var(--sachet-ink); gap: 4px; }
  .sachet .tagline .sep { height: 12px; }
  .serving-badge {
    position: absolute; left: 131px; top: 261px; width: 29px; height: 29px;
    border-radius: 50%; background: var(--beet); color: var(--white);
    font-family: "Montserrat", sans-serif; text-align: center;
  }
  .serving-badge .num { display: block; font-size: 15px; line-height: 19px; }
  .serving-badge .label { display: block; font-size: 4px; letter-spacing: 0.5px; }
</style>
</head>
<body>
<main class="canvas">

  <section class="box" aria-label="Box front">
    <div class="brand"><span class="brand-dot"></span><span class="brand-name">VELOROOT</span></div>
    <h1 class="headline">Beetroot Nitrate<br>Supplement</h1>
    <p class="tagline">BUILD <span class="sep"></span> PERFORM <span class="sep"></span> RECOVER</p>
    <p class="count">4 Sachets</p>
    <div class="sport-icons" role="img" aria-label="Swimming, cycling and running icons"><span></span><span></span><span></span></div>
    <div class="beet-illustration" role="img" aria-label="Beetroot illustration with leaves"></div>
  </section>

  <section class="sachet" aria-label="Sachet">
    <svg class="sachet-face" width="189" height="312" viewBox="0 0 189 312">
      <defs>
        <linearGradient id="sachetSheen" x1="0" y1="0" x2="1" y2="0">
          <stop offset="0" stop-color="#e6e6e6"/>
          <stop offset="0.35" stop-color="#ffffff"/>
          <stop offset="1" stop-color="#ececec"/>
        </linearGradient>
        <linearGradient id="sachetBlack" x1="0" y1="0" x2="1" y2="0">
          <stop offset="0" stop-color="#111"/>
          <stop offset="0.3" stop-color="#3a3a3a"/>
          <stop offset="0.6" stop-color="#141414"/>
          <stop offset="1" stop-color="#1c1c1c"/>
        </linearGradient>
      </defs>
      <rect width="189" height="312" fill="url(#sachetSheen)"/>
      <polygon points="0,0 189,0 189,85 0,223" fill="url(#sachetBlack)"/>
    </svg>
    <div class="brand"><span class="brand-dot"></span><span class="brand-name">VELOROOT</span></div>
    <h2 class="headline">Beetroot Nitrate<br>Supplement</h2>
    <p class="tagline">BUILD <span class="sep"></span> PERFORM <span class="sep"></span> RECOVER</p>
    <div class="serving-badge"><span class="num">1</span><span class="label">SERVING</span></div>
  </section>

</main>
</body>
</html>
```